standardize print collateral

we need help standardizing all print collateral and website. top priorities:

1. standardized case studies template
2. standardized marketing slicks template
3. standardized powerpoint template
Updates

Project Deadline Extended
Reason: We are extending the project to allow current design submissions to be tweaked while providing the opportunity for new designs to be submitted. We will need all 3 collateral designs submitted to make a final decision. Please note, these 3 designs should all look different, needless to say they should all compliment eachother. As for some direction, the powerpoint main color should not be yellow since yellow does not show up the same shade on any screen. The case study and marketing slicks will be printed and often sit next to our competitors marketing material - think high end product, technology, revolutionary, edgy, professional. The designs should compliment eachother and feel like the Brightfern Metrics brand (which you are determining) and should stand out professionally. We are open to introducing new colors into our brand, the only thing that must remain the same is our logo. Have fun, make it edgy, and keep it professional. Looking forward to seeing what you submit!

Target Market(s)

Property Casualty Insurance Companies: Executive level wording with actuarial credibility

Industry/Entity Type

Marketing

Requirements
Must have
• professional layout for existing collateral and 2-page marketing slicks. style guide/colors can be transferred to powerpoint. logo must stay; everything else (i.e. color, font, layout/structure etc.) is flexible. The three components should not looks the same, they should only compliment eachother.
Nice to have
• we are revolutionizing a conservative industry, so adequate level of edgy/advanced technology/impactful feel to layout
Should not have
• no need to stay within color constraints of yellow, but need to appropriately work well with the eagle head logo

```html
<!DOCTYPE html>
<html lang="en">
<head>
<meta charset="utf-8">
<title>Brightfern Metrics — Print Collateral</title>
<link href="https://fonts.googleapis.com/css2?family=PT+Sans:wght@400;700&family=PT+Sans+Narrow:wght@400;700&display=swap" rel="stylesheet">
<style>
:root{
  --ink:#111111;
  --ink-soft:#2a2a2a;
  --gold:#f3b80a;
  --amber:#e19a08;
  --cream:#fcf4c6;
  --butter:#f8e37a;
  --paper:#e4e4e4;
  --grey-hi:#f2f2f2;
  --grey-lo:#a9a9a9;
  --photo:#5c430c;
  --heat-red:#e0433a;
  --heat-org:#f29a3a;
  --heat-yel:#f5dc5a;
  --heat-grn:#69b84f;
  --text:#222222;
}
*{box-sizing:border-box;margin:0;padding:0}
html,body{width:1200px;height:900px;overflow:hidden}
body{background:var(--paper);font-family:"PT Sans",Arial,sans-serif;color:var(--text);position:relative}

.sheet{position:absolute;top:204px;width:380px;height:492px;overflow:hidden;box-shadow:0 2px 8px rgba(0,0,0,.25)}
.sheet > *{position:absolute}
.sheet--case{left:18px;background:radial-gradient(ellipse at 55% 45%,#fffbe4 0%,var(--cream) 45%,var(--butter) 100%)}
.sheet--slick-back{left:410px;background:radial-gradient(ellipse at 50% 40%,#fffbe0 0%,#fbee9e 55%,#f5d85a 100%)}
.sheet--slick-front{left:802px;background:linear-gradient(180deg,var(--grey-hi) 0%,#d6d6d6 55%,var(--grey-lo) 100%)}

.brand{display:flex;align-items:center;gap:4px;font-weight:700;font-size:9px;line-height:1.05;color:var(--ink)}
.brand__dot{width:14px;height:14px;border-radius:50%;background:var(--gold);flex:none}

.header-photo{background:var(--photo)}

.title-block{color:var(--gold);font-weight:700;text-align:center;line-height:1.1}

.banner{border-radius:9px;background:linear-gradient(180deg,#fbd34a 0%,var(--amber) 100%);border:1px solid #b37405;box-shadow:0 1px 2px rgba(0,0,0,.35);font-weight:700;color:var(--ink);text-align:center;font-size:7px;line-height:1.2;display:flex;align-items:center;justify-content:center;padding:0 10px}

.section-head{display:block;background:var(--ink);color:var(--gold);font-weight:700;font-size:7.5px;padding:2px 5px;margin:6px 0 3px;border-radius:0 6px 0 0}
.copy{font-size:5.6px;line-height:1.35;color:var(--text)}
.copy p{margin-bottom:4px}
.copy ul{padding-left:10px;margin-top:2px}

.chart-box{background:#fff;border:1px solid #999}
.caption{font-size:4.6px;line-height:1.3;text-align:center}
.caption--dark{background:var(--ink);color:#f3e6b0;padding:2px 4px}

.closing{background:var(--ink);border-radius:26px 0 0 0;color:var(--gold);font-size:6px;line-height:1.35}
.closing__text{position:absolute}
.address{color:var(--ink);font-size:5px;line-height:1.4}
.footer{left:0;right:0;bottom:0;height:22px;background:var(--ink);color:#fff;font-weight:700;display:flex;align-items:center;justify-content:space-between;padding:0 14px;font-size:8.5px}
.footer span{white-space:nowrap}

.lead{font-size:5.6px;line-height:1.3;color:var(--ink);text-align:center}
.lead strong{font-size:7.6px}
.how{background:linear-gradient(180deg,#fbd34a 0%,var(--amber) 100%);border:1px solid #9b6404;border-radius:6px;padding:3px 5px;color:var(--ink)}
.how h2{font-size:12px;text-align:center;background:linear-gradient(180deg,#fde48a,#f3b80a);border-radius:4px;margin-bottom:4px}
.how h3{font-size:6.5px;margin-top:5px}
.how h3 em{font-style:normal;background:var(--ink);color:var(--gold);padding:0 3px;margin-right:3px}
.how p{font-size:5.2px;line-height:1.3}
.panel-title{background:var(--ink);color:var(--gold);font-weight:700;font-size:7.5px;padding:2px 5px;border-radius:0 6px 0 0}
.heat{border-collapse:collapse;width:100%;font-family:"PT Sans Narrow",Arial,sans-serif;font-size:3.8px;background:#fff}
.heat th{background:var(--gold);color:var(--ink);padding:1px}
.heat td{border:0.5px solid #ccc;padding:0.8px 1px;text-align:center}
.heat .r{background:var(--heat-red)}.heat .o{background:var(--heat-org)}.heat .y{background:var(--heat-yel)}.heat .g{background:var(--heat-grn)}
.closing-band{background:var(--ink);border-radius:0 18px 0 0;color:var(--gold);font-size:5.6px;padding:5px 8px}
.report-note{background:#2b2b2b;color:#fff;font-size:5.2px;line-height:1.35;padding:5px 8px}
</style>
</head>
<body>

<section class="sheet sheet--case" aria-label="Case study sheet">
  <div class="brand" style="left:10px;top:18px"><span class="brand__dot"></span><span>Brightfern<br>Metrics</span></div>
  <div style="left:100px;top:0;width:280px;height:70px;background:var(--ink)"></div>
  <div class="header-photo" role="img" aria-label="Header photograph of a golden light burst" style="left:270px;top:0;width:110px;height:70px"></div>
  <div class="title-block" style="left:104px;top:10px;width:170px">
    <div style="font-size:17px">Case Study</div>
    <div style="font-size:8.5px">Private Passenger Auto</div>
    <div style="font-size:8.5px">Revised Rating Plan</div>
  </div>
  <div class="banner" style="left:70px;top:77px;width:280px;height:22px">27% lift added to state's largest domestic<br>property and casualty insurance company</div>

  <div class="copy" style="left:10px;top:104px;width:176px">
    <span class="section-head">Project Objective</span>
    <p>The insurer decided to completely revise their rating plan and introduce it as a new program. In designing the new rating plan, all factors were considered:</p>
    <ul><li>New base rates</li><li>Rating factors</li><li>Territory definitions and relativities</li></ul>
    <span class="section-head">Our Approach</span>
    <p>The approach incorporated the strengths of both Vireo GLM and Vireo Complete Segmentation.</p>
    <p>Vireo's GLM was used to build an initial model for the bulk of the class plan and to control for certain other fields (e.g. geographic effects). Residuals from this initial GLM were analyzed by Vireo's Complete Segmentation to discover the compound variables undetected by the GLM framework.</p>
    <p>Given the new compound variables along with the initial GLM, Vireo's Complete Segmentation was used again to explore geographic fields to determine new territory definitions.</p>
  </div>
  <div class="copy" style="left:196px;top:96px;width:174px">
    <span class="section-head">Timeframe</span>
    <p>This project was extensive, involving territory definitions, base rates, and rating plan factors for five different coverages. The timeline spanned approximately six months using Brightfern's powerful software solution suite.</p>
    <span class="section-head">Product Advantages</span>
    <p>Vireo's GLM uniqueness and superior results derive from its integration with Vireo's powerful Complete Segmentation capabilities. The combined solution streamlines and accelerates the process of building rating plans while providing greater accuracy than traditional GLMs.</p>
    <span class="section-head">Results</span>
    <p>The Complete Segmentation analysis added 27% lift to the GLM model, with an average correlation of 95.8%, indicating a very high degree of consistency on unseen validation data. The new rating plan was filed and approved by the state Department of Insurance. With more accurate rates in place, the insurer is positioned for profitable growth.</p>
  </div>

  <svg style="left:8px;top:330px" width="180" height="92" viewBox="0 0 180 92" aria-label="Lorenz curve from initial GLM model">
    <text x="95" y="7" font-size="4.5" text-anchor="middle" fill="#222">Lorenz curve from initial GLM model</text>
    <defs><linearGradient id="lorenzBg" x1="0" y1="0" x2="0" y2="1"><stop offset="0" stop-color="#5f97d6"/><stop offset="1" stop-color="#c9def3"/></linearGradient></defs>
    <rect x="18" y="10" width="156" height="68" fill="url(#lorenzBg)"/>
    <g stroke="#ffffff" stroke-opacity=".5" stroke-width=".5"><line x1="18" y1="24" x2="174" y2="24"/><line x1="18" y1="38" x2="174" y2="38"/><line x1="18" y1="52" x2="174" y2="52"/><line x1="18" y1="66" x2="174" y2="66"/></g>
    <line x1="18" y1="78" x2="174" y2="10" stroke="#1b3b6b" stroke-width=".8"/>
    <path d="M18 78 C40 40 80 20 174 10" fill="none" stroke="#0c2446" stroke-width="1.2"/>
    <g font-size="4" fill="#222" text-anchor="middle"><text x="18" y="84">0</text><text x="49" y="84">20</text><text x="80" y="84">40</text><text x="112" y="84">60</text><text x="143" y="84">80</text><text x="174" y="84">100</text></g>
    <text x="6" y="50" font-size="4" transform="rotate(-90 6 50)" text-anchor="middle" fill="#222">Cumulative Estimates (%)</text>
  </svg>
  <svg style="left:190px;top:330px" width="184" height="92" viewBox="0 0 184 92" aria-label="Segmentation model for territory definitions">
    <text x="98" y="7" font-size="4.5" text-anchor="middle" fill="#222">Segmentation model for territory definitions</text>
    <polygon points="18,14 34,10 180,10 180,72 18,78" fill="#9a9a9a"/>
    <polygon points="18,78 180,72 180,78 18,84" fill="#d28a2a"/>
    <g fill="#2e9a57">
      <rect x="24" y="64" width="8" height="14"/><rect x="37" y="62" width="8" height="16"/><rect x="50" y="61" width="8" height="17"/><rect x="63" y="60" width="8" height="18"/><rect x="76" y="58" width="8" height="20"/><rect x="89" y="56" width="8" height="22"/><rect x="102" y="53" width="8" height="25"/><rect x="115" y="50" width="8" height="28"/><rect x="128" y="46" width="8" height="32"/><rect x="141" y="40" width="8" height="38"/><rect x="154" y="30" width="8" height="48"/><rect x="167" y="18" width="8" height="60"/>
    </g>
    <g font-size="4" fill="#222" text-anchor="middle"><text x="28" y="90">5</text><text x="54" y="90">11</text><text x="80" y="90">6</text><text x="106" y="90">7</text><text x="132" y="90">12</text><text x="158" y="90">4</text><text x="171" y="90">1</text></g>
    <text x="8" y="48" font-size="4" transform="rotate(-90 8 48)" text-anchor="middle" fill="#222">Loss Ratio %</text>
  </svg>

  <div class="closing" style="left:0;top:425px;width:248px;height:67px">
    <p class="closing__text" style="left:16px;top:8px;width:220px">Brightfern Metrics provides breakthrough predictive analytics powered by machine learning and the latest statistical techniques, enabling property and casualty insurers to achieve superior performance.</p>
  </div>
  <div class="address" style="left:262px;top:434px">214 Harlow Avenue, Suite 310<br>Marlow, SC 29480</div>
  <div class="footer"><span>www.brightfernmetrics.com</span><span>PH: 555.014.2290</span><span>F: 555.014.2291</span></div>
</section>

<section class="sheet sheet--slick-back" aria-label="Marketing slick page two">
  <div style="left:0;top:0;width:380px;height:62px;background:var(--ink)"></div>
  <div class="header-photo" role="img" aria-label="Header photograph of a golden light burst" style="left:130px;top:0;width:130px;height:62px"></div>
  <div class="banner" style="left:30px;top:72px;width:320px;height:24px">Vireo detects, measures and presents actionable options to<br>correct the effects of adverse selection within any P&amp;C portfolio.</div>

  <svg class="chart-box" style="left:14px;top:110px" width="168" height="96" viewBox="0 0 168 96" aria-label="Bar chart of loss ratio by score band">
    <g stroke="#ddd" stroke-width=".5"><line x1="16" y1="20" x2="162" y2="20"/><line x1="16" y1="40" x2="162" y2="40"/><line x1="16" y1="60" x2="162" y2="60"/></g>
    <g fill="#3f7fc4"><rect x="24" y="26" width="12" height="52"/><rect x="46" y="34" width="12" height="44"/><rect x="68" y="42" width="12" height="36"/><rect x="90" y="50" width="12" height="28"/><rect x="112" y="54" width="12" height="24"/><rect x="134" y="58" width="12" height="20"/></g>
    <line x1="16" y1="78" x2="162" y2="78" stroke="#888" stroke-width=".5"/>
    <g font-size="3.8" fill="#333" text-anchor="middle"><text x="30" y="84">0-100</text><text x="52" y="84">101-250</text><text x="74" y="84">251-400</text><text x="96" y="84">401-550</text><text x="118" y="84">551-700</text><text x="140" y="84">701-900</text><text x="88" y="92">Score Band</text></g>
  </svg>
  <svg class="chart-box" style="left:198px;top:110px" width="168" height="96" viewBox="0 0 168 96" aria-label="Bubble chart of loss ratio against quality score">
    <g stroke="#ddd" stroke-width=".5"><line x1="20" y1="20" x2="162" y2="20"/><line x1="20" y1="50" x2="162" y2="50"/><line x1="20" y1="66" x2="162" y2="66"/></g>
    <line x1="20" y1="34" x2="162" y2="28" stroke="#3f7fc4" stroke-width="1"/>
    <g fill="#a9c6ea" stroke="#3f7fc4" stroke-width=".6"><circle cx="60" cy="50" r="6"/><circle cx="66" cy="42" r="5"/><circle cx="72" cy="34" r="6"/><circle cx="150" cy="18" r="7"/></g>
    <g font-size="4" fill="#1b3b6b" text-anchor="middle"><text x="60" y="51.5">2</text><text x="66" y="43.5">4</text><text x="72" y="35.5">3</text><text x="150" y="19.5">1</text></g>
    <g font-size="3.8" fill="#333" text-anchor="middle"><text x="24" y="78">-10%</text><text x="68" y="78">-5%</text><text x="112" y="78">0%</text><text x="156" y="78">5%</text><text x="92" y="90">Quality Score</text></g>
    <text x="8" y="46" font-size="3.8" transform="rotate(-90 8 46)" text-anchor="middle" fill="#333">Loss Ratio</text>
  </svg>
  <p class="caption caption--dark" style="left:14px;top:210px;width:168px">Discover the pricing imbalances within the portfolio. These imbalances are the main driver of the adverse selection.</p>
  <p class="caption caption--dark" style="left:198px;top:210px;width:168px">Show trends within the portfolio in real time covering premium adequacy and the quality of all business being written.</p>

  <div class="banner" style="left:14px;top:238px;width:352px;height:28px;background:var(--ink-soft);color:var(--gold);border-color:#000">Report on detailed analyses including sales trend and profitability trends. This allows for a<br>method of managing distribution channels while addressing pricing imbalances</div>

  <svg class="chart-box" style="left:30px;top:282px" width="150" height="92" viewBox="0 0 150 92" aria-label="Line chart of portfolio score over time">
    <g stroke="#ddd" stroke-width=".5"><line x1="18" y1="16" x2="146" y2="16"/><line x1="18" y1="30" x2="146" y2="30"/><line x1="18" y1="44" x2="146" y2="44"/><line x1="18" y1="58" x2="146" y2="58"/></g>
    <path d="M20 30 L28 24 L36 27 L44 22 L52 26 L60 23 L68 28 L76 24 L84 27 L92 25 L100 35 L108 31 L116 40 L124 36 L132 44 L140 40" fill="none" stroke="#3f7fc4" stroke-width="1"/>
    <g font-size="3.4" fill="#333" text-anchor="end"><text x="16" y="18">600</text><text x="16" y="32">500</text><text x="16" y="46">400</text><text x="16" y="60">300</text></g>
    <g font-size="3.2" fill="#333"><text x="22" y="80" transform="rotate(-90 22 80)">Jan</text><text x="48" y="80" transform="rotate(-90 48 80)">Apr</text><text x="74" y="80" transform="rotate(-90 74 80)">Jul</text><text x="100" y="80" transform="rotate(-90 100 80)">Oct</text><text x="126" y="80" transform="rotate(-90 126 80)">Dec</text></g>
  </svg>
  <svg class="chart-box" style="left:200px;top:282px" width="150" height="92" viewBox="0 0 150 92" aria-label="Bar chart of percent change by segment">
    <g stroke="#ddd" stroke-width=".5"><line x1="22" y1="14" x2="146" y2="14"/><line x1="22" y1="60" x2="146" y2="60"/><line x1="22" y1="74" x2="146" y2="74"/></g>
    <line x1="22" y1="36" x2="146" y2="36" stroke="#888" stroke-width=".5"/>
    <g fill="#3f7fc4"><rect x="34" y="36" width="12" height="5"/><rect x="62" y="36" width="12" height="32"/><rect x="92" y="18" width="12" height="18"/><rect x="120" y="26" width="12" height="10"/></g>
    <g font-size="3.6" fill="#333" text-anchor="end"><text x="20" y="16">60%</text><text x="20" y="38">0%</text><text x="20" y="62">-40%</text><text x="20" y="76">-60%</text></g>
    <text x="84" y="86" font-size="3.8" fill="#333" text-anchor="middle">Segment Number</text>
  </svg>

  <div class="closing" style="left:0;top:398px;width:262px;height:94px">
    <p class="closing__text" style="left:26px;top:14px;width:220px;font-size:6.4px">Through the use of these advanced analytics your company has the opportunity to future proof each of your portfolios.</p>
  </div>
  <div class="address" style="left:276px;top:412px">214 Harlow Avenue, Suite 310<br>Marlow, SC 29480</div>
  <div class="footer"><span>www.brightfernmetrics.com</span><span>PH: 555.014.2290</span><span>F: 555.014.2291</span></div>
</section>

<section class="sheet sheet--slick-front" aria-label="Marketing slick page one">
  <div class="brand" style="left:12px;top:18px"><span class="brand__dot"></span><span>Brightfern<br>Metrics</span></div>
  <div style="left:100px;top:8px;width:280px;height:62px;background:var(--ink)"></div>
  <div class="header-photo" role="img" aria-label="Header photograph of a golden light burst" style="left:290px;top:8px;width:90px;height:62px"></div>
  <div class="title-block" style="left:104px;top:20px;width:186px">
    <div style="font-size:13px">Rapid Portfolio Analysis</div>
    <div style="font-size:7.5px">Winning Against Adverse Selection</div>
  </div>
  <p class="lead" style="left:12px;top:76px;width:356px"><strong>The property and casualty market is over-supplied with excess capacity,</strong> and current pricing methods are inconsistent and outdated. This leads to a considerable level of adverse selection within nearly every portfolio. Almost every insurer is attracting customers who are underpriced and losing business where they are overpriced. This invisible effect only surfaces after evidence of slowly deteriorating portfolio loss ratios, resulting in premium increases across the portfolio. These across-the-board premium increases exacerbate the problem by overpricing the most profitable customers and driving them into the arms of competitors.</p>

  <div class="how" style="left:8px;top:148px;width:176px;height:158px">
    <h2>How does it work?</h2>
    <h3><em>Detection:</em>Is the portfolio priced correctly?</h3>
    <p>Vireo employs a regression method based on a technological breakthrough. It exposes pricing imbalances by commonly employed rating methods including the GLM. These pricing imbalances are the major drivers of adverse selection.</p>
    <h3><em>Measurement:</em>How is the portfolio trending?</h3>
    <p>Vireo scores the two most important attributes of the portfolio: the adequacy of rates and the quality of the business on a progressive basis. In addition, Vireo projects the financial outcome of business as it is written with startling accuracy. Insurers are able to know significantly in advance of trends in their business.</p>
    <h3><em>Correction:</em>How to address the issues?</h3>
    <p>Vireo provides an array of options for addressing any deterioration in the portfolio. These options range from specifically designed rate adjustments and underwriting strategies, to simple distribution management sales and profitability strategies.</p>
  </div>

  <div style="left:192px;top:148px;width:180px">
    <div class="panel-title">Portfolio Monitoring</div>
    <table class="heat">
      <tr><th>Year</th><th>Premium</th><th>Losses</th><th>Ratio</th><th>Score</th></tr>
      <tr><td>2006</td><td>$1.21M</td><td>$0.64M</td><td class="g">53%</td><td>412</td></tr>
      <tr><td>2007</td><td>$1.34M</td><td>$0.78M</td><td class="y">58%</td><td>398</td></tr>
      <tr><td>2008</td><td>$1.40M</td><td>$0.91M</td><td class="o">65%</td><td>371</td></tr>
      <tr><td>2009</td><td>$1.47M</td><td>$1.06M</td><td class="r">72%</td><td>344</td></tr>
      <tr><td>2010</td><td>$1.52M</td><td>$0.93M</td><td class="o">61%</td><td>366</td></tr>
      <tr><td>2011</td><td>$1.60M</td><td>$0.86M</td><td class="g">54%</td><td>405</td></tr>
    </table>
    <p class="caption" style="margin-top:2px">Predict the future loss ratio of the business being written - both renewals and new business</p>
  </div>
  <div style="left:192px;top:232px;width:180px">
    <div class="panel-title">Distribution Monitoring</div>
    <table class="heat">
      <tr><th>Agent</th><th>Premium</th><th>Losses</th><th>Ratio</th><th>Score</th></tr>
      <tr><td>A-01</td><td>$412K</td><td>$198K</td><td class="g">48%</td><td>421</td></tr>
      <tr><td>A-02</td><td>$388K</td><td>$225K</td><td class="y">58%</td><td>392</td></tr>
      <tr><td>A-03</td><td>$351K</td><td>$239K</td><td class="o">68%</td><td>360</td></tr>
      <tr><td>A-04</td><td>$297K</td><td>$229K</td><td class="r">77%</td><td>331</td></tr>
      <tr><td>A-05</td><td>$276K</td><td>$143K</td><td class="g">52%</td><td>410</td></tr>
      <tr><td>A-06</td><td>$244K</td><td>$151K</td><td class="y">62%</td><td>384</td></tr>
    </table>
    <p class="caption" style="margin-top:2px">Constantly track the quality and performance of individual distribution outlets based on the underwriting score of each policy</p>
  </div>

  <div class="closing-band" style="left:0;top:322px;width:380px;height:40px">We should create a closing statement here.</div>
  <p class="report-note" style="left:0;top:362px;width:380px;height:130px">Let Brightfern Metrics Build Your Portfolio Analysis Report. The report details your portfolio trends and identifies future unseen problems before they occur. The insight provided in the report exhibits what is actually going on in your portfolio. This likely includes adverse selection, impact of price changes with unintended consequences, and the emerging trends in the composition of the book. The analysis results not only reveal past trends, but also predict future impact.</p>
</section>

</body>
</html>
```